Create a Graphic About YOURSELF and PixelHarbor

PixelHarbor would like you (designers) to create an awesome graphic to promote YOURSELF and your profile on PixelHarbor!

Your graphic should communicate your name, your services and should mention PixelHarbor.

The design should be perfect for sharing on Chatterly. Here's an example of what we'd like http://blog.pixelharbor-example.ca/article/333/pixelharbor-launches-3000-hire-me-social-design-contest

Once you submitted your design, we'd love you to share the design ('advertisement') and promote yourself and PixelHarbor to your friends and potential customers. So make your submissions great and get your friends to vote for your design by 'Liking' it on Chatterly!

Prizes:
$1500 - "PixelHarbor Community" prize awarded to the designer with the most Chatterly 'Likes'
5 x $50 for the next 5 'most liked' designs on Chatterly

$1000 - "Hire Me" prize awarded to the designer who receives the most client invites
5 x $50 for the next 5 'most invited' designers

In summary, this is a great opportunity for you to increase your exposure to PixelHarbor customers and win cash prizes. Show off your design skills and get hired by PixelHarbor customers from around the world!

Target Market(s)

Fans, friends and customers of YOU

Industry/Entity Type

Cash

Requirements
Must have
• 1) Include your PixelHarbor user name on the graphic so customers can find you in the PixelHarbor Designer Directory
2) Include the tagline "Hire Me on PixelHarbor.com!" in your graphic design.
3) Share your design's URL on our Chatterly wall at http://chatterly-example.com/pixelharbor and get your friends to 'like' your design.
Nice to have
• 1) Include a tagline that expresses your design approach/philosophy
2) Artwork dimensions: 403 x 403 px
3) You can submit more than 1 design!
Should not have
• You must own the copyright of any images you use including stock imagery.

```html
<!DOCTYPE html>
<html lang="en">
<head>
<meta charset="utf-8">
<title>Be Lumora – Hire Me on PixelHarbor.com</title>
<link rel="stylesheet" href="https://fonts.googleapis.com/css2?family=Michroma&family=Pathway+Gothic+One&family=Josefin+Sans:wght@300&display=swap">
<style>
  :root {
    --ink: #070808;
    --panel: #141515;
    --glow: #1f4d55;
    --teal: #2e6a72;
    --cyan: #3bbcc8;
    --lime: #7dff1a;
    --white: #ffffff;
    --disc: #f2f4f6;
  }
  * { margin: 0; padding: 0; box-sizing: border-box; }
  html, body { width: 924px; height: 1200px; overflow: hidden; background: var(--ink); }
  .poster { position: relative; width: 924px; height: 1200px; overflow: hidden; background: var(--ink); }
  .glow-frame {
    position: absolute; left: 40px; top: 130px; width: 850px; height: 1000px;
    background: radial-gradient(ellipse at center, var(--glow) 0%, #0f2c31 55%, transparent 75%);
    filter: blur(18px);
  }
  .panel {
    position: absolute; left: 165px; top: 165px; width: 630px; height: 900px;
    background: var(--panel);
    box-shadow: 0 0 40px 20px rgba(10,12,12,0.9);
  }
  .tagline-lead {
    position: absolute; left: 91px; top: 48px;
    font: 400 24px "Michroma", sans-serif; color: var(--white); letter-spacing: 1px; white-space: nowrap;
  }
  .tagline-main {
    position: absolute; left: 437px; top: 92px;
    font: 400 56px "Michroma", sans-serif; color: var(--lime); letter-spacing: 2px; white-space: nowrap;
  }
  .disc { position: absolute; border-radius: 50%; background: var(--disc); border: 3px solid #222; box-shadow: 3px 4px 6px rgba(0,0,0,.6); }
  .disc.small { background: var(--ink); border: 2px solid var(--white); box-shadow: none; }
  .pebble { position: absolute; border-radius: 50%; background: var(--teal); }
  .brand-name {
    position: absolute; left: 205px; width: 550px; top: 525px; text-align: center;
    font: 400 160px/1 "Pathway Gothic One", sans-serif; color: var(--white); letter-spacing: 18px;
  }
  .brand-sub {
    position: absolute; left: 545px; top: 714px;
    font: 400 44px/1 "Pathway Gothic One", sans-serif; color: var(--cyan); letter-spacing: 2px;
  }
  .services {
    position: absolute; left: 25px; top: 662px; list-style: none; color: var(--white);
    font-family: "Pathway Gothic One", sans-serif;
  }
  .services li { font-size: 50px; line-height: 66px; white-space: nowrap; }
  .services li:first-child { font-size: 62px; line-height: 72px; }
  .services li:nth-child(2) { padding-left: 6px; }
  .services li:nth-child(3) { padding-left: 4px; }
  .hire {
    position: absolute; left: 338px; top: 1000px;
    font: 300 64px/1 "Josefin Sans", sans-serif; color: var(--lime);
    font-variant: small-caps; letter-spacing: 12px; white-space: nowrap;
  }
  .site {
    position: absolute; left: 0; width: 924px; top: 1124px; text-align: center;
    font: 400 30px/1 "Michroma", sans-serif; color: var(--white); letter-spacing: 9px; white-space: nowrap;
  }
</style>
</head>
<body>
<main class="poster">
  <div class="glow-frame"></div>
  <div class="panel"></div>

  <p class="tagline-lead">Don't Be Generic,</p>
  <h1 class="tagline-main">Be Lumora</h1>

  <div class="pebble" style="left:98px;top:133px;width:34px;height:44px;transform:rotate(30deg)"></div>
  <div class="pebble" style="left:835px;top:1030px;width:50px;height:40px;transform:rotate(-30deg)"></div>

  <div class="disc" style="left:268px;top:88px;width:92px;height:92px"></div>
  <div class="disc" style="left:145px;top:205px;width:80px;height:80px"></div>
  <div class="disc" style="left:68px;top:320px;width:76px;height:76px"></div>
  <div class="disc" style="left:52px;top:474px;width:68px;height:68px"></div>
  <div class="disc small" style="left:833px;top:518px;width:38px;height:38px"></div>
  <div class="disc small" style="left:825px;top:610px;width:38px;height:38px"></div>
  <div class="disc small" style="left:776px;top:686px;width:42px;height:42px"></div>
  <div class="disc small" style="left:700px;top:760px;width:46px;height:46px"></div>

  <p class="brand-name">Lumora</p>
  <p class="brand-sub">Designz</p>

  <ul class="services">
    <li>Logos.</li>
    <li>Bizcards.</li>
    <li>Fliers.</li>
    <li>Brochures</li>
    <li>Stationary.</li>
    <li>Invitations..</li>
  </ul>

  <p class="hire">Hire Me</p>
  <p class="site">on PixelHarbor.com</p>
</main>
</body>
</html>
```